Flyer-Design für Bücherei
Zielgruppe
Wir sind eine ehrenamtlich geführte Bücherei in Talbrunn. Wir bieten unseren Kunden eine professionell geführte Bücherei im moderne Stil mit mind. 30 neuen Medien pro Woche. Unsere Zielgruppe sind die Bewohner in Talbrunn, vor allen Kinder, Familien mit Kindern und Senioren.
Wir haben über 12.000 Medien, bestehend aus Bilderbücher, Kinderbücher, Jugendliteratur, Romane, Hörbücher für Kinder, Wupsel, Reiseführer, Zeitschriften, Spiele und Sachliteratur für Kinder und Jugendliche. Wir haben einen online Katalog und unsere Kunden können online ihre ausgeliehen Medien sehen und verlängern, sowie Vormerkungen platzieren.
Neben den Büchereibetrieb bieten wir Regelmäßige Autorenlesungen, Vorleseaktionen für Kinder, Bastelabende und Führungen für Schul- und Kindergartengruppen.
Ziele des Fördervereins sind:
- Die Bücherei als Kultur-, Bildungs- und Freizeiteinrichtung unterstützen und erhalten
- Durch Öffentlichkeitsarbeit die Bücherei stärker im Bewusstsein der Bevölkerung verankern
- Maßnahmen zur Verbesserung der Leistungsfähigkeit und Attraktivität der Bücherei ergreifen
- Veranstaltung fördern und organisieren
- Neue Freunde und Förderer für die Bücherei gewinnen
Aufgabenstellung
Öffnungszeiten:
Montag, Donnerstag, Freitag 15:00 - 18:00
Kontaktdaten:
Telefon: 07041-57-306
E-Mail: info@lesestube-talbrunn.de
Online-Katalog: online.lesestube-talbrunn.de
Das Design soll schön und ansprechend sein. Es soll ein zwei mal gefalzter Flyer im Din lang Format sein. Wenn er zusammengefaltet ist soll es eine Startseite geben wo Förderverein der Bücherei Talbrunn e.V. drauf steht und auf der Rückseite die Öffnungszeiten und Kontaktdaten.
Bitte formulieren Sie gerne die Texte um, so das die Texte zum Design des Flyers passen . Wir sind eine moderne und aktuelle Bücherei und wollen so auch im Flyer auftreten. Aktuell haben wir nur die Akzentfarbe Rot ansonsten sind wir bei Schwarz und Weiß, wie sie auch im Logo sehen.
Wenn der Flyer uns überzeugt, sind wir gewillt auch noch zwei Roll-Ups designen zu lassen, sowie in Zukunft mit ihnen weiter zusammen zuarbeiten.

```html
<!DOCTYPE html>
<html lang="de">
<head>
<meta charset="utf-8">
<title>Flyer – Bücherei Talbrunn</title>
<link rel="stylesheet" href="https://fonts.googleapis.com/css2?family=EB+Garamond:wght@400;500;600&display=swap">
<style>
:root{
  --stage:#d8d9db;
  --ink:#ffffff;
  --ink-soft:rgba(255,255,255,.82);
  --deep:#1b2f6e;
  --navy:#233a86;
  --teal:#1f8fae;
  --aqua:#5cc3d6;
  --sky:#9fd3e2;
  --accent:#d62a2a;
}
*{box-sizing:border-box;margin:0;padding:0}
html,body{width:1200px;height:630px;overflow:hidden}
body{background:var(--stage);font-family:"EB Garamond",Georgia,serif;color:var(--ink);position:relative}
.sheet{position:absolute;top:112px;width:570px;height:404px;display:flex;box-shadow:0 10px 28px rgba(0,0,0,.22)}
.sheet--outer{left:20px}
.sheet--inner{left:610px}
.panel{position:relative;width:190px;height:100%;overflow:hidden;padding:22px 16px;
  background:radial-gradient(circle at 30% 20%,rgba(92,195,214,.55),transparent 55%),
             radial-gradient(circle at 75% 80%,rgba(35,58,134,.9),transparent 60%),
             linear-gradient(160deg,var(--teal),var(--navy) 70%,var(--deep))}
.panel + .panel{border-left:1px solid rgba(255,255,255,.12)}
.panel--light{background:radial-gradient(circle at 60% 30%,rgba(159,211,226,.5),transparent 55%),
             linear-gradient(170deg,var(--aqua),var(--teal) 45%,var(--navy))}
h2{font-weight:500;font-size:25px;line-height:1.05;margin-bottom:8px}
h3{font-weight:500;font-size:21px;line-height:1.05;margin-bottom:4px}
p,li{font-size:10.5px;line-height:1.4;color:var(--ink-soft)}
ul{list-style:none}
li{margin-bottom:5px;padding-left:8px;position:relative}
li::before{content:"·";position:absolute;left:0}
.icon{display:block;stroke:var(--ink);fill:none;stroke-width:2;stroke-linecap:round;stroke-linejoin:round}
.goal-icon{margin:6px 0 10px}
.block{margin-bottom:18px}
.catalog-icon{margin-bottom:8px}
.photo{position:absolute;left:0;right:0}
.photo--book{top:0;height:62%;background:linear-gradient(165deg,#cfe3ec,#6f9cb6 45%,#2c4f78)}
.photo--stack{top:0;height:46%;background:linear-gradient(150deg,#3d5d8a,#7a6a4a 55%,#a78a52)}
.photo--kids{bottom:0;height:50%;background:linear-gradient(200deg,#e7cdb4,#d7a3a6 40%,#5f9fb3)}
.brand{position:absolute;top:26px;left:16px;right:16px;display:flex;align-items:center;gap:8px}
.brand-mark{width:14px;height:14px;background:var(--accent);flex:none}
.brand-name{font-size:22px;font-weight:600;color:#111;line-height:1}
.cover-title{position:absolute;left:16px;right:16px;bottom:24px}
.cover-title h2{font-size:24px}
.media-head{font-size:26px;font-weight:500;margin-bottom:14px}
.media-grid{display:grid;grid-template-columns:repeat(3,1fr);gap:14px 6px;text-align:center}
.media-item span{display:block;font-size:9.5px;line-height:1.15;margin-top:4px;color:var(--ink-soft)}
.media-item svg{margin:0 auto}
.stack-arrow{position:absolute;left:22px;top:120px}
.weekly{position:absolute;left:16px;right:16px;top:200px}
.events{position:relative}
</style>
</head>
<body>

<section class="sheet sheet--outer" aria-label="Außenseite">
  <article class="panel panel--goals">
    <svg class="icon goal-icon" width="56" height="56" viewBox="0 0 56 56" aria-hidden="true">
      <circle cx="28" cy="32" r="22"/><circle cx="28" cy="32" r="14"/><circle cx="28" cy="32" r="6"/>
      <path d="M28 32V4M22 10l6-6 6 6"/>
    </svg>
    <h2>Ziele des Fördervereins sind:</h2>
    <ul>
      <li>Die Bücherei als Kultur-, Bildungs- und Freizeiteinrichtung unterstützen und erhalten</li>
      <li>Durch Öffentlichkeitsarbeit die Bücherei stärker im Bewusstsein der Bevölkerung verankern</li>
      <li>Maßnahmen zur Verbesserung der Leistungsfähigkeit und Attraktivität der Bücherei ergreifen</li>
      <li>Veranstaltung fördern und organisieren</li>
      <li>Neue Freunde und Förderer für die Bücherei gewinnen</li>
    </ul>
  </article>

  <article class="panel panel--info">
    <div class="block">
      <svg class="icon catalog-icon" width="60" height="44" viewBox="0 0 60 44" aria-hidden="true">
        <rect x="3" y="6" width="34" height="24" rx="2"/><path d="M9 14h16M9 20h22M9 26h12"/>
        <path d="M38 18l16 6-7 2-2 7z"/><path d="M44 6l-2 5M52 8l-4 4M56 16h-5"/>
      </svg>
      <h3>Online-Katalog</h3>
      <p>Sie können Ihre ausgeliehen Medien online sehen und verlängern, sowie Vormerkungen platzieren.</p>
    </div>
    <div class="block">
      <h3>Öffnungszeiten</h3>
      <p>Montag, Donnerstag, Freitag:<br>15:00 – 18:00</p>
    </div>
    <div class="block">
      <h3>Kontakt</h3>
      <p>Telefon: 07041-57-306<br>E-Mail: info@lesestube-talbrunn.de<br>Online-Katalog: online.lesestube-talbrunn.de</p>
    </div>
  </article>

  <article class="panel panel--light panel--cover">
    <div class="photo photo--book" role="img" aria-label="Foto eines aufgeschlagenen Buches mit fächernden Seiten"></div>
    <div class="brand"><span class="brand-mark"></span><span class="brand-name">Bücherei Talbrunn</span></div>
    <div class="cover-title">
      <h2>Förderverein der Bücherei Talbrunn e.V.</h2>
    </div>
  </article>
</section>

<section class="sheet sheet--inner" aria-label="Innenseite">
  <article class="panel panel--light panel--media">
    <p class="media-head">12.000 Medien</p>
    <div class="media-grid">
      <div class="media-item"><svg class="icon" width="30" height="26" viewBox="0 0 30 26"><path d="M15 5C11 2 6 2 2 3v19c4-1 9-1 13 2 4-3 9-3 13-2V3c-4-1-9-1-13 2zM15 5v19"/></svg><span>Bilderbücher</span></div>
      <div class="media-item"><svg class="icon" width="30" height="26" viewBox="0 0 30 26"><rect x="4" y="3" width="22" height="20" rx="2"/><path d="M15 3v20"/></svg><span>Kinderbücher</span></div>
      <div class="media-item"><svg class="icon" width="30" height="26" viewBox="0 0 30 26"><rect x="3" y="3" width="24" height="20" rx="2"/><path d="M7 8h7M7 12h7M7 16h7M17 8h6M17 12h6M17 16h6"/></svg><span>Jugendliteratur</span></div>
      <div class="media-item"><svg class="icon" width="30" height="26" viewBox="0 0 30 26"><rect x="7" y="2" width="17" height="22" rx="1"/><path d="M11 7h9M11 11h9"/></svg><span>Romane</span></div>
      <div class="media-item"><svg class="icon" width="30" height="26" viewBox="0 0 30 26"><path d="M4 16a11 11 0 0 1 22 0"/><rect x="2" y="15" width="5" height="8" rx="2"/><rect x="23" y="15" width="5" height="8" rx="2"/></svg><span>Hörbücher für Kinder</span></div>
      <div class="media-item"><svg class="icon" width="30" height="26" viewBox="0 0 30 26"><rect x="7" y="4" width="16" height="20" rx="3"/><circle cx="15" cy="14" r="4"/></svg><span>Wupsel</span></div>
      <div class="media-item"><svg class="icon" width="30" height="26" viewBox="0 0 30 26"><path d="M3 5l8-2 8 2 8-2v18l-8 2-8-2-8 2zM11 3v18M19 5v18"/></svg><span>Reiseführer</span></div>
      <div class="media-item"><svg class="icon" width="30" height="26" viewBox="0 0 30 26"><rect x="5" y="3" width="16" height="20" rx="1"/><path d="M21 6h4v17H9M9 8h8M9 12h8"/></svg><span>Zeitschriften</span></div>
      <div class="media-item"><svg class="icon" width="30" height="26" viewBox="0 0 30 26"><rect x="4" y="4" width="22" height="18" rx="2"/><path d="M9 17l3-9 3 9M10 14h4M18 9h5l-5 8h5"/></svg><span>Spiele und Sachliteratur</span></div>
    </div>
  </article>

  <article class="panel panel--weekly">
    <div class="photo photo--stack" role="img" aria-label="Foto eines wachsenden Stapels bunter Bücher"></div>
    <svg class="icon stack-arrow" width="60" height="60" viewBox="0 0 60 60" aria-hidden="true"><path d="M4 56C24 48 42 30 52 8M42 10l10-2 2 10"/></svg>
    <div class="weekly">
      <h2>30 neuen Medien pro Woche</h2>
      <p>Wir sind eine ehrenamtlich geführte Bücherei in Talbrunn. Wir bieten Ihnen eine professionell geführte Bücherei im modernen Stil mit mind. 30 neuen Medien pro Woche.</p>
    </div>
  </article>

  <article class="panel panel--light panel--events">
    <div class="events">
      <h2>Veranstaltungen</h2>
      <p>Autorenlesungen, Vorleseaktionen für Kinder, Bastelabende und Führungen für Schul- und Kindergartengruppen.</p>
    </div>
    <div class="photo photo--kids" role="img" aria-label="Foto einer Vorleserin mit einer Gruppe lauschender Kinder"></div>
  </article>
</section>

</body>
</html>
```